Business Card Design Project

I am a property development company requiring a professional looking business card.
The name of the my company is KLV SUMMITRA. I have attached a couple of designs that I have created on my own, that can give you an idea of what I am after.
Above the wording KLV SUMMITRA, I have a orange arc above these words to signify the sun is begining to rise above the horizon.
I have a few designs; Middle Rays, Side Rays, Horizontals Rays which are OK, but I am looking for the better design.
The Rear design of the card is what I had came up with. If you have a better design, I am happy to see it.
The design of the card can follow what I have came up with, or it can be totally different. The fonts needs to be adjusted to another font that is more suitable.
The colours that I have used is what I think I would like to stick with. As I have mentioned, the orange arc is to signify the sun rising. If you have a better colour scheme, I would consider it.
Looking at dealing with first home buyers and proffesional people.
Business

```html
<!DOCTYPE html>
<html lang="en">
<head>
<meta charset="utf-8">
<title>KLV Summitra – Business Card</title>
<link rel="stylesheet" href="https://fonts.googleapis.com/css2?family=Arimo&family=Kaushan+Script&family=Abril+Fatface&display=swap">
<style>
  :root {
    --paper: #ffffff;
    --ink: #333333;
    --ink-soft: #2b2b2b;
    --border: #555555;
    --sun-red: #ec3b2a;
    --sun-orange: #f5842a;
    --sun-yellow: #fdcb2a;
    --arc: #f2844c;
    --arc-fade: rgba(242, 132, 76, 0);
  }
  html, body {
    margin: 0;
    padding: 0;
    width: 1200px;
    height: 735px;
    overflow: hidden;
    background: var(--paper);
  }
  .card {
    position: relative;
    width: 1200px;
    height: 735px;
    background: var(--paper);
  }
  .card-art {
    position: absolute;
    inset: 0;
    width: 1200px;
    height: 735px;
  }
  .sunrise-mark {
    position: absolute;
    left: 296px;
    top: 279px;
    width: 610px;
    height: 40px;
    background: linear-gradient(to bottom, var(--arc), var(--arc-fade));
  }
  .contact {
    position: absolute;
    margin: 0;
    font-family: "Arimo", Arial, sans-serif;
    color: var(--ink-soft);
  }
  .contact span { display: block; white-space: nowrap; }
  .contact-address {
    left: 20px;
    top: 63px;
    font-size: 40px;
    line-height: 41px;
  }
  .contact-address .line-small { font-size: 36px; }
  .contact-address .line-phone { font-size: 41px; }
  .contact-online {
    right: 21px;
    top: 68px;
    text-align: right;
    font-size: 35px;
    line-height: 36px;
  }
  .person {
    position: absolute;
    left: 0;
    right: 0;
    top: 334px;
    text-align: center;
    color: var(--ink);
  }
  .person-name {
    margin: 0;
    font-family: "Kaushan Script", cursive;
    font-size: 72px;
    font-weight: 400;
    line-height: 1;
    letter-spacing: 2px;
  }
  .person-role {
    margin: 2px 0 0;
    font-family: "Abril Fatface", serif;
    font-size: 64px;
    line-height: 1;
    letter-spacing: 3px;
  }
  .company-name, .company-line {
    font-family: "Abril Fatface", serif;
    fill: var(--ink);
  }
</style>
</head>
<body>
<main class="card">
  <svg class="card-art" viewBox="0 0 1200 735" aria-hidden="true">
    <defs>
      <linearGradient id="band-top" x1="0" y1="0" x2="0" y2="1">
        <stop offset="0" stop-color="var(--sun-red)"/>
        <stop offset="0.25" stop-color="var(--sun-orange)"/>
        <stop offset="0.6" stop-color="var(--sun-yellow)"/>
        <stop offset="1" stop-color="var(--sun-yellow)"/>
      </linearGradient>
      <linearGradient id="band-bottom" x1="0" y1="0" x2="0" y2="1">
        <stop offset="0" stop-color="var(--sun-yellow)"/>
        <stop offset="0.55" stop-color="var(--sun-yellow)"/>
        <stop offset="0.85" stop-color="var(--sun-orange)"/>
        <stop offset="1" stop-color="var(--sun-red)"/>
      </linearGradient>
    </defs>
    <g transform="scale(1.1385 1.1378)">
      <rect class="card-frame" x="2" y="38" width="1050" height="607" fill="var(--paper)"/>
      <path class="band-top" d="M2 38 H1052 V52 C880 70 760 120 560 170 C350 222 170 240 2 322 Z" fill="url(#band-top)"/>
      <path class="band-bottom" d="M2 612 C220 575 430 535 640 490 C800 458 940 444 1052 446 V645 H2 Z" fill="url(#band-bottom)"/>
      <rect class="card-frame-line" x="2" y="38" width="1050" height="607" fill="none" stroke="var(--border)" stroke-width="1.5"/>
    </g>
    <text class="company-name" x="552" y="651" font-size="72" textLength="624" lengthAdjust="spacingAndGlyphs">KLV SUMMITRA</text>
    <text class="company-line" x="552" y="706" font-size="42" textLength="624" lengthAdjust="spacingAndGlyphs">PROPERTY DEVELOPMENTS</text>
  </svg>

  <div class="sunrise-mark" role="img" aria-label="Orange rising-sun arc above the director's name"></div>

  <p class="contact contact-address">
    <span>27 Kestrel Rd Alford</span>
    <span class="line-small">N.S.W. Australia 2291</span>
    <span class="line-phone">Mob: 0412 555 309</span>
  </p>

  <p class="contact contact-online">
    <span>Email: marcus@klvsummitra.com</span>
    <span>Web: www.klvsummitra.com</span>
  </p>

  <section class="person">
    <h1 class="person-name">Marcus Lowe</h1>
    <p class="person-role">DIRECTOR</p>
  </section>
</main>
</body>
</html>
```